I teach courses in Quick Phrases for Rescue Crews, paramedics, firefighters, nurses and all other Emergency related occupations. I need to let them know that this course is available and post this card on the bulletin boards of fire stations and other related offices. It has to call their attention.

Industry/Entity Type

Call

Colors
ec2027

Requirements
Must have
• I would like a picture of a paramedic and a nurse. It can also have a firefighter as a second choice. Red is a good color to call attention. I am including a picture of me and a short bio to go on the reverse but this is not a must. I do not want my picture in the front.
I am thinking of an over sized postcard
Nice to have
• The title can be "Quick Phrases for Rescue Crews" in full or "Quick Phrases for RC's " depending on the fact that the whole name may be too long to make it stand out enough
Should not have
• I do not know if my picture has come out in the right frame I see the cut is not right in the uploead. You might need to frame it right.

```html
<!DOCTYPE html>
<html lang="en">
<head>
<meta charset="utf-8">
<title>Quick Phrases for Rescue Crews</title>
<link rel="stylesheet" href="https://fonts.googleapis.com/css2?family=Questrial&family=Poppins:wght@300;600;700&display=swap">
<style>
  :root {
    --red: #ec2027;
    --blue: #0f6fbf;
    --ink: #2b2b2b;
    --white: #ffffff;
    --body-light: #f7f7f7;
    --body-dark: #d4d5d7;
    --backdrop: #e9e6e2;
    --frame: #8a8a8a;
  }
  * { box-sizing: border-box; margin: 0; padding: 0; }
  html, body {
    width: 1200px; height: 1000px; overflow: hidden;
    background: var(--backdrop);
  }
  .postcard {
    position: absolute; left: 50px; top: 75px;
    width: 1100px; height: 850px;
    background: radial-gradient(ellipse at 50% 40%, var(--body-light) 0%, #ececed 55%, var(--body-dark) 100%);
    box-shadow: 0 4px 14px rgba(0,0,0,0.35);
    font-family: "Questrial", "Century Gothic", sans-serif;
    color: var(--ink);
  }
  .title-band {
    height: 157px; background: var(--red);
    border-bottom: 10px solid var(--blue);
    text-align: center; color: var(--white);
    padding-top: 24px;
  }
  .title-lead {
    font-family: "Poppins", sans-serif; font-weight: 300;
    font-size: 42px; line-height: 48px; letter-spacing: -0.5px;
  }
  .title-main {
    font-family: "Poppins", sans-serif; font-weight: 600;
    font-size: 56px; line-height: 62px; letter-spacing: -1px;
  }
  .audience {
    text-align: center; font-size: 28px; line-height: 36px;
    margin-top: 20px;
  }
  .audience strong {
    color: var(--red); font-family: "Poppins", sans-serif; font-weight: 600;
    font-size: 26px;
  }
  .benefits {
    list-style: none; margin: 22px 0 0 65px;
  }
  .benefits li {
    position: relative; padding-left: 52px;
    font-size: 23px; line-height: 31.4px;
  }
  .benefits li::before {
    content: ""; position: absolute; left: 0; top: 6px;
    width: 20px; height: 20px; border-radius: 50%;
    border: 3px solid var(--red);
    background: radial-gradient(circle, var(--red) 0 4px, var(--white) 5px);
  }
  .photo-row {
    position: absolute; top: 537px; left: 32px; right: 32px;
    display: flex; gap: 12px;
  }
  .photo {
    flex: 1; height: 162px; border: 2px solid var(--frame);
  }
  .photo-nurse { background: linear-gradient(135deg, #f1f3f6 0%, #c9d9ea 50%, #3f6fa8 100%); }
  .photo-firefighter { background: radial-gradient(ellipse at 30% 40%, #f7b12c 0%, #d9631a 45%, #4a1d0c 100%); }
  .photo-paramedics { background: linear-gradient(120deg, #1f3d78 0%, #3b5fa1 45%, #c9ad93 70%, #5b6f8e 100%); }
  .location-band {
    position: absolute; top: 720px; left: 0; right: 0; height: 75px;
    background: var(--red); color: var(--white); text-align: center;
    font-size: 25px; line-height: 31px; padding-top: 7px;
  }
  .location-band strong { font-family: "Poppins", sans-serif; font-weight: 600; font-size: 24px; }
  .contact-band {
    position: absolute; top: 795px; left: 0; right: 0; height: 55px;
    background: var(--blue); color: var(--white); text-align: center;
    font-size: 20px; line-height: 55px;
  }
  .contact-band strong { font-family: "Poppins", sans-serif; font-weight: 600; font-size: 19px; }
</style>
</head>
<body>
  <main class="postcard">
    <header class="title-band">
      <h1>
        <span class="title-lead" style="display:block">Quick Phrases for</span>
        <span class="title-main" style="display:block">Rescue Crews</span>
      </h1>
    </header>

    <p class="audience">Course designed specifically for <strong>paramedics, firefighters, nurses</strong><br>and all other <strong>emergency related occupations.</strong></p>

    <ul class="benefits">
      <li>Learn exactly the language you need for each emergency situation</li>
      <li>Bring down the language barrier with your Spanish-speaking patients</li>
      <li>Earn credits for your job or resume</li>
      <li>Meet new people while you practice</li>
      <li>Build a solid base for speaking Spanish in any situation sounding like a native</li>
      <li>Learn easily with " whole brain learning tools"</li>
      <li>Learn more about yourself and how you learn best</li>
      <li>Have great fun and de-stress</li>
    </ul>

    <div class="photo-row">
      <div class="photo photo-nurse" role="img" aria-label="Photo of a nurse in blue scrubs holding a clipboard"></div>
      <div class="photo photo-firefighter" role="img" aria-label="Photo of firefighters in turnout gear facing flames"></div>
      <div class="photo photo-paramedics" role="img" aria-label="Photo of paramedics performing CPR on a patient"></div>
    </div>

    <p class="location-band">Small groups and one-on-one coaching/tutoring sessions available in<br><strong>Santa Monica, California.</strong></p>

    <p class="contact-band">For more information find us on <strong>Linkspace as Marisol Quintero</strong> or <strong>Call: 310 5550147</strong></p>
  </main>
</body>
</html>
```